Business Card Design needed for start up company Pramora

In need of a new business card designed for a start up company based in Sydney, Pramora is a new start up innovative Company, our mission it to make property accessible for everyday Australian and to become the leading Real Estate platform in Australia. We want it to be fresh and clean.

Industry/Entity Type

Financial

Contact Information for Business Card

Section for Name
Section for Title

PRAMORA - Where Doors Open Wide
Mobile:
Direct:

Font styles to use
Sans Serif

Colors
33a6d7
0692cd
0255a3
ffffff

Requirements
Must have
• Logo, all business card details

```html
<!DOCTYPE html>
<html lang="en">
<head>
<meta charset="utf-8">
<title>Pramora Business Cards</title>
<link href="https://fonts.googleapis.com/css2?family=Montserrat:wght@400;500;700;800&family=Oswald:wght@600&display=swap" rel="stylesheet">
<style>
  :root {
    --page-bg: #dcdde0;
    --card-white: #ffffff;
    --brand-blue: #229bd5;
    --brand-navy: #1f4a7e;
    --text-dark: #2a2a2a;
    --divider: #c9c9c9;
  }
  * { box-sizing: border-box; margin: 0; padding: 0; }
  html, body {
    width: 1200px;
    height: 2198px;
    overflow: hidden;
    background: var(--page-bg);
    font-family: "Montserrat", sans-serif;
  }
  .card {
    position: absolute;
    left: 146px;
    width: 907px;
    height: 586px;
    border-radius: 32px;
    background: var(--card-white);
    box-shadow: 0 8px 22px rgba(0,0,0,0.18);
    overflow: hidden;
  }
  .card--contact { top: 145px; }
  .card--brand { top: 797px; }
  .card--brand-blue { top: 1459px; background: var(--brand-blue); }

  .wordmark {
    position: absolute;
    font-family: "Montserrat", sans-serif;
    font-weight: 800;
    color: var(--brand-navy);
    line-height: 1;
    white-space: nowrap;
  }

  /* contact card */
  .card--contact .wordmark {
    left: 54px;
    width: 362px;
    top: 262px;
    font-size: 62px;
    text-align: center;
  }
  .divider {
    position: absolute;
    left: 451px;
    top: 110px;
    width: 2px;
    height: 367px;
    background: var(--divider);
  }
  .person-name {
    position: absolute;
    left: 489px;
    top: 140px;
    font-family: "Oswald", sans-serif;
    font-weight: 600;
    font-size: 36px;
    line-height: 44px;
    color: var(--brand-navy);
    letter-spacing: 0.5px;
  }
  .person-title {
    position: absolute;
    left: 489px;
    top: 186px;
    font-weight: 700;
    font-size: 21px;
    line-height: 24px;
    color: var(--brand-blue);
    letter-spacing: 1px;
  }
  .contact-list {
    position: absolute;
    left: 489px;
    top: 243px;
    list-style: none;
  }
  .contact-list li {
    display: flex;
    align-items: flex-start;
    font-size: 25px;
    line-height: 36px;
    color: var(--text-dark);
    letter-spacing: 0.6px;
  }
  .contact-list svg {
    width: 22px;
    height: 22px;
    margin: 7px 8px 0 0;
    flex: none;
    fill: var(--brand-blue);
  }

  /* brand cards */
  .card--brand .wordmark,
  .card--brand-blue .wordmark {
    left: 0; right: 0;
    top: 235px;
    font-size: 112px;
    text-align: center;
  }
  .card--brand-blue .wordmark { color: var(--card-white); }

  .tagline {
    position: absolute;
    left: 0; right: 0;
    top: 499px;
    text-align: center;
    font-size: 30px;
    line-height: 36px;
    color: var(--text-dark);
    letter-spacing: 0.3px;
  }
  .tagline-band {
    position: absolute;
    left: 0; right: 0;
    top: 475px;
    height: 78px;
    background: var(--brand-navy);
    display: flex;
    align-items: center;
    justify-content: center;
    font-weight: 700;
    font-size: 32px;
    color: var(--card-white);
    letter-spacing: 0.5px;
  }
</style>
</head>
<body>

<section class="card card--contact">
  <span class="wordmark">PRAMORA</span>
  <div class="divider"></div>
  <p class="person-name">YOUR NAME</p>
  <p class="person-title">TITLE</p>
  <ul class="contact-list">
    <li>
      <svg viewBox="0 0 24 24"><path d="M6.6 10.8a15.1 15.1 0 0 0 6.6 6.6l2.2-2.2c.3-.3.7-.4 1-.2 1.1.4 2.3.6 3.6.6.6 0 1 .4 1 1V20c0 .6-.4 1-1 1C10.6 21 3 13.4 3 4c0-.6.4-1 1-1h3.5c.6 0 1 .4 1 1 0 1.3.2 2.5.6 3.6.1.3 0 .7-.2 1l-2.3 2.2z"/></svg>
      123.456.7890
    </li>
    <li>
      <svg viewBox="0 0 24 24"><path d="M7 2h10a2 2 0 0 1 2 2v16a2 2 0 0 1-2 2H7a2 2 0 0 1-2-2V4a2 2 0 0 1 2-2zm0 3v12h10V5H7zm5 13.2a1 1 0 1 0 0 2 1 1 0 0 0 0-2z"/></svg>
      123.456.7890
    </li>
    <li>
      <svg viewBox="0 0 24 24"><path d="M2 5h20v14H2V5zm2 2v.4l8 5.2 8-5.2V7H4zm0 2.8V17h16V9.8l-8 5.2-8-5.2z"/></svg>
      name@Pramora.com.au
    </li>
    <li>
      <svg viewBox="0 0 24 24"><path d="M12 2a10 10 0 1 0 0 20 10 10 0 0 0 0-20zm6.9 6h-3a15.7 15.7 0 0 0-1.4-3.6A8 8 0 0 1 18.9 8zM12 4c.8 1.2 1.5 2.5 1.9 4h-3.8c.4-1.5 1.1-2.8 1.9-4zM4.3 14a8.2 8.2 0 0 1 0-4h3.4a16.5 16.5 0 0 0 0 4H4.3zm.8 2h3a15.7 15.7 0 0 0 1.4 3.6A8 8 0 0 1 5.1 16zm3-8h-3a8 8 0 0 1 4.4-3.6C8.9 5.5 8.4 6.7 8.1 8zM12 20c-.8-1.2-1.5-2.5-1.9-4h3.8c-.4 1.5-1.1 2.8-1.9 4zm2.3-6H9.7a14.7 14.7 0 0 1 0-4h4.6a14.7 14.7 0 0 1 0 4zm.2 5.6c.6-1.1 1.1-2.3 1.4-3.6h3a8 8 0 0 1-4.4 3.6zm1.8-5.6a16.5 16.5 0 0 0 0-4h3.4a8.2 8.2 0 0 1 0 4h-3.4z"/></svg>
      www.Pramora.com.au
    </li>
    <li>
      <svg viewBox="0 0 24 24"><path d="M12 2a7 7 0 0 0-7 7c0 5.3 7 13 7 13s7-7.7 7-13a7 7 0 0 0-7-7zm0 9.5a2.5 2.5 0 1 1 0-5 2.5 2.5 0 0 1 0 5z"/></svg>
      <span>1234 Harbourline Street<br>Sydney NSW 2000</span>
    </li>
  </ul>
</section>

<section class="card card--brand">
  <span class="wordmark">PRAMORA</span>
  <p class="tagline">Where Doors Open Wide</p>
</section>

<section class="card card--brand-blue">
  <span class="wordmark">PRAMORA</span>
  <div class="tagline-band">Where Doors Open Wide</div>
</section>

</body>
</html>
```